Cedar Harbor Business Cards For New Startup

I am looking for you to design some business cards for a new startup https://cedarharborhub.com. I have supplied logo, brand guidelines and our signatures as a guide.

We need this to reflect the brand guidelines and the website for brand consistency,

What is Cedar Harbor?

Mallorca's Business Growth Community
Join your new business community full of passionate entrepreneurs who
love to solve problems and help each other grow together!

Any questions you can ask.

Target Market(s)

Business to Business

Contact Information for Business Card

These are attached (signatures) to the job

Font styles to use
Other font styles liked:
• Open Sans

Requirements
Must have
• Match design guidelines
Nice to have
• Photos of our faces so people remember us

```html
<!DOCTYPE html>
<html lang="en">
<head>
<meta charset="utf-8">
<title>Cedar Harbor Business Cards</title>
<link href="https://fonts.googleapis.com/css2?family=Open+Sans:wght@400;600;700&display=swap" rel="stylesheet">
<style>
  :root {
    --olive: #65692e;
    --olive-dark: #545826;
    --white: #ffffff;
    --ink: #3a3a3a;
    --backdrop: #e8e3d8;
  }
  * { margin: 0; padding: 0; box-sizing: border-box; }
  html, body {
    width: 900px; height: 1200px; overflow: hidden;
    background: var(--backdrop);
    font-family: "Open Sans", Arial, sans-serif;
  }
  .stage { position: relative; width: 900px; height: 1200px; }

  .card {
    position: absolute; left: 82px; width: 733px;
    border-radius: 22px; overflow: hidden;
    box-shadow: 0 6px 14px rgba(0,0,0,0.25);
  }
  .card-front { top: 137px; height: 428px; background: var(--white); }
  .card-back { top: 633px; height: 429px; background: var(--olive); }

  .front-arc { position: absolute; inset: 0; }

  .portrait {
    position: absolute; left: 48px; top: 51px; width: 135px; height: 135px;
    border: 2px solid var(--olive);
    background: linear-gradient(160deg, #c9b9a4 0%, #e6d3a8 45%, #9d8c7a 100%);
  }

  .brand { position: absolute; display: flex; align-items: center; }
  .brand-mark { border-radius: 50%; border: 2px solid currentColor; flex: none; }
  .brand-name { font-weight: 600; letter-spacing: 0.01em; white-space: nowrap; }

  .brand-front { left: 351px; top: 63px; color: var(--olive); }
  .brand-front .brand-mark { width: 64px; height: 64px; margin-right: 26px; }
  .brand-front .brand-name { font-size: 33px; }

  .identity { position: absolute; left: 47px; top: 266px; }
  .person-name { font-size: 22px; color: var(--olive); font-weight: 400; line-height: 1.2; }
  .person-name strong { font-weight: 700; }
  .person-role { font-size: 15.5px; color: var(--ink); margin-top: 3px; }

  .contact { position: absolute; left: 47px; top: 328px; font-size: 16.5px; color: var(--ink); }
  .contact-row { display: flex; align-items: center; height: 24px; }
  .contact-row svg { width: 20px; margin-right: 6px; }

  .social { position: absolute; right: 47px; top: 335px; display: flex; gap: 3px; }
  .social-square { width: 34px; height: 34px; background: var(--olive); }

  .front-band {
    position: absolute; left: 0; right: 0; bottom: 0; height: 33px;
    background: var(--olive); color: var(--white);
    font-size: 16.5px; font-weight: 600;
    display: flex; align-items: center; justify-content: center;
  }

  .brand-back { left: 50%; top: 172px; transform: translateX(-50%); color: var(--white); }
  .brand-back .brand-mark { width: 96px; height: 96px; margin-right: 32px; border-width: 2.5px; }
  .brand-back .brand-name { font-size: 48px; }

  .back-url {
    position: absolute; left: 0; right: 0; top: 378px; text-align: center;
    color: var(--white); font-size: 16.5px; letter-spacing: 0.32em; font-weight: 400;
  }
</style>
</head>
<body>
<main class="stage">
  <section class="card card-front">
    <svg class="front-arc" width="733" height="428" viewBox="0 0 733 428" aria-hidden="true">
      <circle cx="540" cy="50" r="236" fill="none" stroke="var(--olive)" stroke-width="3"/>
    </svg>

    <div class="portrait" role="img" aria-label="Portrait photo of Helena Marsh"></div>

    <div class="brand brand-front">
      <span class="brand-mark"></span>
      <span class="brand-name">CEDAR HARBOR</span>
    </div>

    <div class="identity">
      <p class="person-name"><strong>HELENA</strong> MARSH</p>
      <p class="person-role">RELATIONSHIP DIRECTOR | CEDAR HARBOR</p>
    </div>

    <div class="contact">
      <p class="contact-row">
        <svg viewBox="0 0 20 22" height="22" aria-hidden="true"><rect x="5" y="1" width="11" height="20" rx="2" fill="none" stroke="var(--olive)" stroke-width="2"/><circle cx="10.5" cy="17" r="1.2" fill="var(--olive)"/></svg>
        +44 7700 900 123
      </p>
      <p class="contact-row">
        <svg viewBox="0 0 20 14" height="14" aria-hidden="true"><rect x="2" y="2" width="16" height="11" fill="var(--olive)"/><path d="M2 2 L10 8 L18 2" fill="none" stroke="var(--white)" stroke-width="1.5"/></svg>
        hm@cedarharborhub.com
      </p>
    </div>

    <div class="social" aria-hidden="true">
      <span class="social-square"></span>
      <span class="social-square"></span>
      <span class="social-square"></span>
      <span class="social-square"></span>
      <span class="social-square"></span>
    </div>

    <div class="front-band">www.cedarharborhub.com</div>
  </section>

  <section class="card card-back">
    <div class="brand brand-back">
      <span class="brand-mark"></span>
      <span class="brand-name">CEDAR HARBOR</span>
    </div>
    <p class="back-url">WWW.CEDARHARBORHUB.COM</p>
  </section>
</main>
</body>
</html>
```